Ecard for facebook and Instagram postings

I need 4 ecards (don't know if that is what it is called) for Facebook and Instagram postings. My Logo and company name should be incorporated and also be square. I would like to be able to insert text as I need. Examples are:

https://www.pictoralhub.com/photo.php?fbid=20262841672382489&set=a.20261729249182489.516031.71298967488&type=1&relevant_count=1

https://media-b-ord.yy.imgvaultcdn.net/hpics-tin4/2345967_657092986477056_308792573_n.jpg

I don't necessarily need images on them, just the color scheme to my business cards and the logo and business name. But if you'd like to give it an interesting look, you can go ahead and play with it. My site is lunaroakcoaching.com, if you'd like to see the style of it.

Thank you!!!
Updates

I just uploaded the logo in two variations.  Thank you!

Target Market(s)

Women 16-65

Industry/Entity Type

Business

Requirements
Must have
• Logo and business name
Should not have
• No white background. I have attached business card picture so you can have an idea of what I'd like.

```html
<!DOCTYPE html>
<html lang="en">
<head>
<meta charset="utf-8">
<title>Luna Oak Coaching – Social Cards</title>
<link href="https://fonts.googleapis.com/css2?family=Montserrat:wght@500;600;700&display=swap" rel="stylesheet">
<style>
  :root {
    --orange: #f7962a;
    --orange-soft: #fbd2a2;
    --pale: #f9cb94;
    --pale-soft: #fde6cb;
    --red: #c8202a;
    --rust: #b8583a;
    --slate: #4f5964;
    --white: #ffffff;
    --url: #8a5a3a;
  }
  html, body {
    margin: 0;
    padding: 0;
    width: 1200px;
    height: 1000px;
    overflow: hidden;
    background: var(--white);
    font-family: "Montserrat", sans-serif;
  }
  .canvas {
    position: relative;
    width: 1200px;
    height: 1000px;
  }
  .card {
    position: absolute;
    width: 360px;
    height: 360px;
    overflow: hidden;
    background: radial-gradient(circle at 50% 50%, var(--white) 0%, var(--orange-soft) 28%, var(--orange) 68%);
  }
  .card--a { left: 121px; top: 70px; }
  .card--b { left: 720px; top: 70px; }
  .card--c { left: 121px; top: 570px; }
  .card--d {
    left: 720px; top: 570px;
    background: radial-gradient(circle at 50% 50%, var(--white) 0%, var(--pale-soft) 30%, var(--pale) 68%);
  }

  /* large faint brand name standing in the centre of each card */
  .brand-feature {
    position: absolute;
    left: 50px;
    top: 40px;
    width: 260px;
    height: 260px;
    display: flex;
    flex-direction: column;
    align-items: center;
    justify-content: center;
    font-size: 86px;
    font-weight: 600;
    line-height: 0.95;
    letter-spacing: -1px;
    text-align: center;
    opacity: 0.45;
  }
  .card--a .brand-feature,
  .card--c .brand-feature { color: var(--rust); }
  .card--b .brand-feature,
  .card--d .brand-feature { color: var(--white); opacity: 0.8; }
  .brand-feature-ring {
    position: absolute;
    left: 60px;
    top: 30px;
    width: 240px;
    height: 240px;
    border-radius: 50%;
    border: 1px solid var(--white);
    opacity: 0.7;
  }
  .card--a .brand-feature-ring { border-color: var(--rust); opacity: 0.6; }

  .footer-rule {
    position: absolute;
    left: 0;
    top: 319px;
    width: 360px;
    height: 3px;
  }
  .card--a .footer-rule { background: var(--red); }
  .card--b .footer-rule { background: var(--white); }
  .card--c .footer-rule { background: var(--slate); }
  .card--d .footer-rule { background: var(--orange); }
  .brand-mark {
    position: absolute;
    left: 19px;
    top: 303px;
    width: 32px;
    height: 32px;
    border-radius: 50%;
    background: var(--orange);
    box-shadow: 0 0 0 2px var(--white);
  }
  .brand-name {
    position: absolute;
    left: 11px;
    top: 340px;
    font-size: 10px;
    font-weight: 600;
    line-height: 12px;
    color: var(--red);
    white-space: nowrap;
  }
  .tagline {
    position: absolute;
    right: 11px;
    top: 332px;
    font-size: 7.5px;
    font-weight: 600;
    line-height: 9px;
    letter-spacing: 1.5px;
    color: var(--slate);
    white-space: nowrap;
  }
  .card--c .tagline,
  .card--d .tagline { color: var(--red); }
  .site {
    position: absolute;
    right: 11px;
    top: 347px;
    font-size: 5.5px;
    font-weight: 500;
    line-height: 7px;
    letter-spacing: 2.2px;
    color: var(--url);
    white-space: nowrap;
  }
</style>
</head>
<body>
<main class="canvas">
  <section class="card card--a">
    <div class="brand-feature-ring"></div>
    <div class="brand-feature"><span>Luna</span><span>Oak</span></div>
    <div class="footer-rule"></div>
    <div class="brand-mark"></div>
    <div class="brand-name">Luna Oak</div>
    <div class="tagline">COACHING SERVICES</div>
    <div class="site">lunaroakcoaching.com</div>
  </section>
  <section class="card card--b">
    <div class="brand-feature-ring"></div>
    <div class="brand-feature"><span>Luna</span><span>Oak</span></div>
    <div class="footer-rule"></div>
    <div class="brand-mark"></div>
    <div class="brand-name">Luna Oak</div>
    <div class="tagline">COACHING SERVICES</div>
    <div class="site">lunaroakcoaching.com</div>
  </section>
  <section class="card card--c">
    <div class="brand-feature-ring"></div>
    <div class="brand-feature"><span>Luna</span><span>Oak</span></div>
    <div class="footer-rule"></div>
    <div class="brand-mark"></div>
    <div class="brand-name">Luna Oak</div>
    <div class="tagline">COACHING SERVICES</div>
    <div class="site">lunaroakcoaching.com</div>
  </section>
  <section class="card card--d">
    <div class="brand-feature-ring"></div>
    <div class="brand-feature"><span>Luna</span><span>Oak</span></div>
    <div class="footer-rule"></div>
    <div class="brand-mark"></div>
    <div class="brand-name">Luna Oak</div>
    <div class="tagline">COACHING SERVICES</div>
    <div class="site">lunaroakcoaching.com</div>
  </section>
</main>
</body>
</html>
```